Flyer für Immobilienmakler
Zielgruppe
Wir, die Wendtal Immobilien GmbH, vermitteln Häuser, Wohnungen und Grundstücke, unsere Zielgruppe sind Verkäufer und Kaufinteressenten aus der Region, Immobilien zur Vermittlung gesucht
Aufgabenstellung
Unverbindliche Ersteinschätzung, Ansprechpartner vor Ort, regionale Marktkenntnis. Max. Din A 5, Immobilien zur Vermittlung gesucht.
- Flyer nur zur Immobilienvermittlung

```html
<!DOCTYPE html>
<html lang="de">
<head>
<meta charset="utf-8">
<title>Wendtal Immobilien – Flyer</title>
<link rel="stylesheet" href="https://fonts.googleapis.com/css2?family=Playfair+Display:wght@500&family=Arimo:wght@400;700&family=Open+Sans:wght@400&display=swap">
<style>
  :root{
    --stage:#5b5764;
    --paper:#ffffff;
    --purple:#6f5aa5;
    --green:#13a37f;
    --lilac:#e4def3;
    --ink:#1f1d24;
    --body:#55525c;
    --sky:#b9cde3;
  }
  *{margin:0;padding:0;box-sizing:border-box}
  html,body{width:1200px;height:1200px;overflow:hidden;background:var(--stage)}
  .flyer{
    position:absolute;left:204px;top:40px;width:842px;height:1191px;
    transform:scale(0.94);transform-origin:0 0;
    background:var(--paper);overflow:hidden;
    font-family:"Arimo",Arial,sans-serif;color:var(--body);
  }
  .hero{position:absolute;left:0;top:0;width:842px;height:640px}
  .brand{
    position:absolute;left:560px;top:100px;
    font-family:"Playfair Display",Georgia,serif;font-weight:500;font-size:15px;
    color:var(--ink);display:flex;align-items:center;gap:8px;letter-spacing:.3px
  }
  .brand-mark{width:10px;height:10px;background:var(--green)}
  .serif{font-family:"Playfair Display",Georgia,serif;font-weight:500;color:var(--ink)}
  .headline{
    position:absolute;left:48px;top:470px;font-size:52px;line-height:48px;letter-spacing:-1.6px
  }
  .col-left{position:absolute;left:48px;top:660px;width:380px}
  .section-title{font-size:21px;line-height:26px;letter-spacing:-.4px;margin-bottom:12px}
  .col-left p,.why p{font-size:16px;line-height:20px;margin-bottom:10px}
  .subhead{color:var(--ink);font-size:17px;margin:-2px 0 6px}
  .service{margin-top:26px}
  .why{
    position:absolute;left:445px;top:660px;width:370px;height:440px;
    background:var(--lilac);border-radius:8px 8px 0 0;padding:30px 24px 0
  }
  .why .section-title{margin-bottom:10px}
  .checklist{list-style:none;margin-bottom:28px}
  .checklist li{position:relative;padding-left:32px;font-size:16px;line-height:20px;margin-bottom:10px}
  .checklist.tight li{margin-bottom:5px}
  .checklist svg{position:absolute;left:8px;top:3px}
  .contact{
    position:absolute;left:0;top:1100px;width:842px;height:91px;background:var(--green);color:#fff
  }
  .contact-label{position:absolute;left:48px;top:18px;font-size:24px;color:#fff;letter-spacing:-.5px}
  .contact-company{position:absolute;left:230px;top:22px;font-family:"Open Sans",Arial,sans-serif;font-size:15px;line-height:23px}
  .contact-company strong{font-family:"Arimo",Arial,sans-serif;font-size:17px}
  .contact-lines{position:absolute;left:538px;top:22px;font-family:"Open Sans",Arial,sans-serif;font-size:15px;line-height:23px}
</style>
</head>
<body>
<main class="flyer">
  <svg class="hero" viewBox="0 0 842 640" aria-hidden="false">
    <defs>
      <linearGradient id="heroTone" x1="0" y1="0" x2="0" y2="1">
        <stop offset="0" stop-color="#9fbde0"/>
        <stop offset=".35" stop-color="#dfe7f0"/>
        <stop offset=".55" stop-color="#a7705e"/>
        <stop offset=".75" stop-color="#5f7a45"/>
        <stop offset="1" stop-color="#6cc3c4"/>
      </linearGradient>
    </defs>
    <polygon role="img" aria-label="Foto: Landhaus mit Ziegeldach, Garten und Pool unter blauem Himmel" points="0,0 842,0 842,612 0,338" fill="url(#heroTone)"/>
    <polygon points="0,330 842,598 842,618 0,344" fill="var(--green)"/>
    <polygon points="0,435 240,356 842,560 842,598 240,394 0,472" fill="var(--purple)"/>
  </svg>

  <div class="brand"><span class="brand-mark"></span>Wendtal Immobilien GmbH</div>

  <h1 class="headline serif">Ihr Regionaler<br>Partner für<br>Immobilienvermittlung</h1>

  <section class="col-left">
    <h2 class="section-title serif">Kompetente Immobilienlösungen<br>Vor Ort</h2>
    <p>Die Wendtal Immobilien GmbH mit Sitz in Wendtal ist Ihr zuverlässiger Ansprechpartner rund um die Vermittlung von Immobilien.</p>
    <p>Mit fundierter regionaler Marktkenntnis und persönlicher Betreuung unterstützen wir Eigentümer, Käufer, Verkäufer sowie Mietinteressenten.</p>
    <div class="service">
      <h2 class="section-title serif">Unsere Leistung</h2>
      <h3 class="subhead">Immobilienvermittlung</h3>
      <p>Ob Verkauf oder Vermietung – wir kümmern uns zuverlässig um die Vermittlung von Häusern, Wohnungen, Grundstücken und Gebäuden.</p>
      <p>Dabei begleiten wir Sie persönlich von der ersten Beratung bis zum erfolgreichen Abschluss.</p>
    </div>
  </section>

  <aside class="why">
    <h2 class="section-title serif">Warum Wendtal Immobilien?</h2>
    <ul class="checklist">
      <li><svg width="14" height="12" viewBox="0 0 14 12"><path d="M2 1l5 5-5 5M7 1l5 5-5 5" fill="none" stroke="var(--purple)" stroke-width="2"/></svg>Persönlicher Ansprechpartner vor Ort</li>
      <li><svg width="14" height="12" viewBox="0 0 14 12"><path d="M2 1l5 5-5 5M7 1l5 5-5 5" fill="none" stroke="var(--purple)" stroke-width="2"/></svg>Umfassende regionale Marktkenntnis</li>
      <li><svg width="14" height="12" viewBox="0 0 14 12"><path d="M2 1l5 5-5 5M7 1l5 5-5 5" fill="none" stroke="var(--purple)" stroke-width="2"/></svg>Transparente und professionelle Abwicklung</li>
      <li><svg width="14" height="12" viewBox="0 0 14 12"><path d="M2 1l5 5-5 5M7 1l5 5-5 5" fill="none" stroke="var(--purple)" stroke-width="2"/></svg>Zuverlässiger Partner für Eigentümer und Investoren</li>
    </ul>
    <h2 class="section-title serif">Immobilien Zur Vermittlung<br>Gesucht</h2>
    <p>Wir sind laufend auf der Suche nach:</p>
    <ul class="checklist tight">
      <li><svg width="14" height="12" viewBox="0 0 14 12"><path d="M2 1l5 5-5 5M7 1l5 5-5 5" fill="none" stroke="var(--purple)" stroke-width="2"/></svg>Häusern</li>
      <li><svg width="14" height="12" viewBox="0 0 14 12"><path d="M2 1l5 5-5 5M7 1l5 5-5 5" fill="none" stroke="var(--purple)" stroke-width="2"/></svg>Wohnungen</li>
      <li><svg width="14" height="12" viewBox="0 0 14 12"><path d="M2 1l5 5-5 5M7 1l5 5-5 5" fill="none" stroke="var(--purple)" stroke-width="2"/></svg>Grundstücken</li>
    </ul>
  </aside>

  <footer class="contact">
    <h2 class="contact-label serif">Kontakt</h2>
    <div class="contact-company"><strong>Wendtal Immobilien GmbH</strong><br>84519 Wendtal, Mühlweg 12</div>
    <div class="contact-lines"><strong>T</strong>: +49 85 99 412380-0<br><strong>E</strong>: kontakt@wendtal-immo.de</div>
  </footer>
</main>
</body>
</html>
```